Landing That Dream Campus Place Might Feel Easier Than Expected! Nine Habits for Raising Report Card Marks an...

I need a cover/front/spine/back for an e-book and a hard cover book that I am publishing on Brindlemart. I have written a book with an eight step process on how to help parents coach their kids to getting grades up and accepted into good colleges. In the book, I am highlighting current day struggles teens and young adults are having with mental health due to the impact of social media. I am helping them understand the impact mental health and social media has had on school stress. I outline a process in my book that my reader can implement herself with her child, or hire me as her coach.

Target Market(s)

Women ages 35 to 55 with teens in high school and college

Industry/Entity Type

Life Coaching

Font styles to use
Serif

Colors

Designer to choose colors to be used in the design.

Requirements
Must have
• Title, name, (credentials/PhD) and simple image on cover. Font and
• point size that you can read in a teeny, tiny thumbnail. Readability is number one goal. Text on thumbnail must be readable. I have been made aware that subtitles are hard to get on E-books.
Nice to have
• Something that immediately lets the reader know what my book is about
Should not have
• No italics or swirly curly font.

```html
<!DOCTYPE html>
<html lang="en">
<head>
<meta charset="utf-8">
<title>Landing That Dream Campus Place – Book Cover</title>
<link rel="stylesheet" href="https://fonts.googleapis.com/css2?family=Bebas+Neue&family=Jost:wght@300;400;600;700&display=swap">
<style>
  :root {
    --page-bg: #ffffff;
    --cover-blue-deep: #0f6fc4;
    --cover-blue: #1b8ad9;
    --cover-glow: #8fe0f2;
    --band-yellow: #fdd07e;
    --accent-yellow: #fbe39a;
    --text-white: #ffffff;
  }
  * { box-sizing: border-box; margin: 0; padding: 0; }
  html, body {
    width: 1200px;
    height: 1200px;
    overflow: hidden;
    background: var(--page-bg);
  }
  .canvas {
    position: relative;
    width: 1200px;
    height: 1200px;
    display: flex;
    align-items: center;
    justify-content: center;
  }
  .cover {
    position: relative;
    width: 690px;
    height: 1140px;
    overflow: hidden;
    background:
      radial-gradient(ellipse 70% 45% at 50% 60%, var(--cover-glow) 0%, rgba(143,224,242,0.55) 35%, rgba(27,138,217,0) 75%),
      linear-gradient(180deg, var(--cover-blue-deep) 0%, var(--cover-blue) 45%, var(--cover-blue) 70%, var(--cover-blue-deep) 100%);
    text-align: center;
    color: var(--text-white);
    font-family: "Jost", sans-serif;
  }
  .author-band {
    height: 112px;
    background: var(--band-yellow);
    display: flex;
    align-items: center;
    justify-content: center;
    font-size: 46px;
    letter-spacing: 0.16em;
    color: var(--text-white);
  }
  .author-name { font-weight: 700; }
  .author-credential { font-weight: 400; margin-left: 0.35em; }
  .title-lead {
    margin-top: 26px;
    font-weight: 300;
    font-size: 54px;
    letter-spacing: 0.06em;
    line-height: 1;
  }
  .title-main {
    margin-top: 10px;
    font-family: "Bebas Neue", sans-serif;
    font-size: 140px;
    line-height: 0.95;
    letter-spacing: 0.01em;
  }
  .title-tail {
    margin-top: 14px;
    font-weight: 300;
    font-size: 42px;
    letter-spacing: 0.06em;
    line-height: 1.25;
    color: var(--accent-yellow);
  }
  .title-tail strong { font-weight: 700; }
  .cover-art {
    display: block;
    margin: 14px auto 0;
    width: 420px;
    height: 480px;
    border-radius: 40px;
    background: radial-gradient(ellipse 55% 60% at 50% 50%, #f4fbfd 0%, #d6eef6 35%, rgba(40,40,44,0.55) 70%, rgba(27,138,217,0) 100%);
  }
  .tagline {
    position: absolute;
    left: 40px;
    right: 40px;
    bottom: 36px;
    font-size: 36px;
    line-height: 1.2;
    font-weight: 400;
  }
  .tagline strong {
    font-weight: 700;
    letter-spacing: 0.08em;
    color: var(--accent-yellow);
  }
</style>
</head>
<body>
  <main class="canvas">
    <section class="cover">
      <header class="author-band">
        <span class="author-name">MARIAN KEEL</span><span class="author-credential">PHD</span>
      </header>
      <h1 class="title">
        <span class="title-lead" style="display:block">LANDING THAT DREAM</span>
        <span class="title-main" style="display:block">CAMPUS PLACE</span>
        <span class="title-tail" style="display:block">MIGHT FEEL <strong>EASIER</strong> THAN<br><strong>EXPECTED</strong></span>
      </h1>
      <div class="cover-art" role="img" aria-label="Light bulb wearing a graduation cap with a gold tassel, glowing against light rays"></div>
      <p class="tagline"><strong>NINE HABITS</strong> for raising report card marks and landing a <strong>DREAM CAMPUS PLACE</strong></p>
    </section>
  </main>
</body>
</html>
```